Family Owned Construction Company Needs Modern Business Cards

We need a new design for our business cards. We are a family owned construction company, Brantwell Construction, based in Mendon, Vermont and would like to add in our new logo and find a more modern look. We also want to use our old to make sure people know who we are. We do site development, highway, environmental, demolition, utility and aggregate.

Contact Information for Business Card

We want to have the office address, 418 Quarry Ridge Road, Alder Falls, NH 03899 and our phone (555) 555-0137 and fax (555) 555-0164 on there as well. Our website is www.brantwellinc.example. There should be a place for the person's name, title, cell number, and email address on the card. Words that we would like to be associated with our company are honesty, predictable, reliable, integrity, dedicated, built right quality, consistent, whatever it takes, and innovation. Safety is also very important to us.

Font styles to use
Serif
Sans Serif
Other font styles liked:
• Square 721 Extented

Colors
0255a3
ffffff

Requirements
Must have
• Office address, phone number and fax number. New logo with excavator
Nice to have
• That we do site development, highway, environmental, demolition, utility, and aggregate. Both logos

```html
<!DOCTYPE html>
<html lang="en">
<head>
<meta charset="utf-8">
<title>Brantwell Construction – Business Cards</title>
<link rel="stylesheet" href="https://fonts.googleapis.com/css2?family=Lato:wght@400;700&family=Arimo:wght@400;700&display=swap">
<style>
  :root {
    --backdrop: #2a2626;
    --navy: #012d5f;
    --navy-ring-1: #022a58;
    --navy-ring-2: #03264f;
    --navy-core: #032247;
    --white: #ffffff;
    --mark-grey: #dcdcdc;
    --icon-bg: #042650;
  }
  * { box-sizing: border-box; margin: 0; padding: 0; }
  html, body {
    width: 1200px; height: 849px; overflow: hidden;
    background: var(--backdrop);
  }
  .sheet { position: relative; width: 1200px; height: 849px; }
  .card {
    position: absolute; top: 277px;
    width: 438px; height: 281px;
    background: var(--navy);
    overflow: hidden;
    color: var(--white);
  }
  .card--front { left: 144px; }
  .card--back { left: 624px; }

  .corner-block { position: absolute; background: var(--white); }
  .card--front .corner-block--top { left: 390px; top: 2px; width: 46px; height: 38px; }
  .card--front .corner-block--bottom { left: 1px; top: 243px; width: 47px; height: 38px; }
  .card--back .corner-block--top { left: 392px; top: 0; width: 45px; height: 36px; }
  .card--back .corner-block--bottom { left: 1px; top: 245px; width: 47px; height: 36px; }

  .halo {
    position: absolute; left: 118px; top: 47px;
    width: 176px; height: 176px; border-radius: 50%;
    background: radial-gradient(circle, #032a57 0 45%, #022b5b 46% 100%);
  }

  .brand {
    position: absolute; left: 14px; top: 12px;
    display: flex; align-items: center; gap: 6px;
    font-family: "Lato", sans-serif; font-weight: 700;
    font-size: 8px; line-height: 1.15; letter-spacing: 0.04em;
    text-transform: uppercase; color: var(--white);
  }
  .brand__square { width: 14px; height: 14px; background: var(--white); flex: none; }

  .person { position: absolute; left: 136px; top: 26px; font-family: "Lato", sans-serif; }
  .person__name { font-size: 17.5px; font-weight: 700; line-height: 1.1; }
  .person__title { font-size: 10.5px; font-weight: 400; margin-top: 2px; }

  .contact { position: absolute; left: 136px; top: 91px; list-style: none; font-family: "Arimo", sans-serif; font-size: 11px; }
  .contact__item { display: flex; align-items: center; height: 19px; margin-bottom: 21px; }
  .contact__item:nth-child(2) { margin-bottom: 20px; }
  .contact__icon {
    width: 19px; height: 19px; border-radius: 50%;
    background: var(--icon-bg);
    display: flex; align-items: center; justify-content: center;
    margin-right: 13px;
  }
  .contact__icon svg { width: 10px; height: 10px; fill: var(--white); }

  .office {
    position: absolute; left: 90px; top: 230px;
    font-family: "Arimo", sans-serif; font-size: 9.2px;
    letter-spacing: 0.04em; word-spacing: 0.12em; line-height: 13px;
    text-transform: uppercase;
  }
  .office__lines { display: flex; }
  .office__fax { margin-left: 32px; }

  .target {
    position: absolute; left: 98px; top: 20px;
    width: 240px; height: 240px; border-radius: 50%;
    background: var(--navy-ring-1);
    display: flex; align-items: center; justify-content: center;
  }
  .target__ring {
    width: 192px; height: 192px; border-radius: 50%;
    background: var(--navy-ring-2);
    display: flex; align-items: center; justify-content: center;
  }
  .target__core {
    width: 152px; height: 152px; border-radius: 50%;
    background: var(--navy-core);
    display: flex; align-items: center; justify-content: center;
  }
  .wordmark {
    font-family: "Lato", sans-serif; font-weight: 700;
    color: var(--mark-grey); text-transform: uppercase;
    text-align: center; font-size: 13px; line-height: 1.25; letter-spacing: 0.08em;
  }
</style>
</head>
<body>
<main class="sheet">
  <section class="card card--front" aria-label="Business card front">
    <div class="halo"></div>
    <div class="corner-block corner-block--top"></div>
    <div class="corner-block corner-block--bottom"></div>

    <div class="brand">
      <span class="brand__square"></span>
      <span>Brantwell<br>Construction</span>
    </div>

    <div class="person">
      <p class="person__name">Daniel Hartwell</p>
      <p class="person__title">CEO</p>
    </div>

    <ul class="contact">
      <li class="contact__item">
        <span class="contact__icon">
          <svg viewBox="0 0 24 24" aria-hidden="true"><path d="M6.6 10.8a15.1 15.1 0 0 0 6.6 6.6l2.2-2.2a1 1 0 0 1 1-.25 11.4 11.4 0 0 0 3.6.57 1 1 0 0 1 1 1V20a1 1 0 0 1-1 1A17 17 0 0 1 3 4a1 1 0 0 1 1-1h3.5a1 1 0 0 1 1 1c0 1.25.2 2.45.57 3.57a1 1 0 0 1-.25 1z"/></svg>
        </span>
        <span>0400&nbsp; 555&nbsp; 219</span>
      </li>
      <li class="contact__item">
        <span class="contact__icon">
          <svg viewBox="0 0 24 24" aria-hidden="true"><path d="M22 2 2 10.5l7 2.5 2.5 7L22 2zM10 13l7-6-5.5 7.5z"/></svg>
        </span>
        <span>daniel@brantwellinc.example</span>
      </li>
      <li class="contact__item">
        <span class="contact__icon">
          <svg viewBox="0 0 24 24" aria-hidden="true"><path d="M12 3 2 12h3v8h5v-6h4v6h5v-8h3z"/></svg>
        </span>
        <span>www.brantwellinc.example</span>
      </li>
    </ul>

    <div class="office">
      <p>Office address: 418 Quarry Ridge Road, Alder Falls, NH 03899</p>
      <p class="office__lines"><span>Phone:(555) 555-0137</span><span class="office__fax">Fax:(555) 555-0164</span></p>
    </div>
  </section>

  <section class="card card--back" aria-label="Business card back">
    <div class="target">
      <div class="target__ring">
        <div class="target__core">
          <p class="wordmark">Brantwell<br>Construction</p>
        </div>
      </div>
    </div>
    <div class="corner-block corner-block--top"></div>
    <div class="corner-block corner-block--bottom"></div>
  </section>
</main>
</body>
</html>
```